Business Cards for wirefen.com.au
Logo already designed by Quillnoxa
Professional
Liam Forbury
Technical Engineer
Mobile: 0437 125 806
liam@wirefen.com.au
www.wirefen.com.au
Should have the text: "Cloud Application Development"

```html
<!DOCTYPE html>
<html lang="en">
<head>
<meta charset="utf-8">
<title>wirefen.com.au — Business Card</title>
<link rel="stylesheet" href="https://fonts.googleapis.com/css2?family=Exo+2:wght@400;600;700&display=swap">
<style>
  :root {
    --page-bg: #eceae6;
    --card-bg: #ffffff;
    --ink-dark: #3a3b3d;
    --ink-grey: #5c5e61;
    --brand-blue: #1f4fa8;
    --brand-blue-light: #2c8fd6;
    --band-grey: #4a4b4d;
    --faint-blue: #e6edf6;
  }
  * { margin: 0; padding: 0; box-sizing: border-box; }
  html, body {
    width: 1200px; height: 935px; overflow: hidden;
    background: var(--page-bg);
    font-family: "Exo 2", sans-serif;
  }
  .card {
    position: absolute; left: 100px; top: 162px;
    width: 1000px; height: 610px;
    background: var(--card-bg);
    border-radius: 44px;
    overflow: hidden;
    box-shadow: 0 18px 40px rgba(0,0,0,0.18);
  }
  .card-decor {
    position: absolute; right: -90px; top: -60px;
    width: 460px; height: 460px; border-radius: 50%;
    background: var(--faint-blue);
  }
  .brand {
    position: absolute; left: 130px; top: 150px;
    display: flex; align-items: center; gap: 18px;
  }
  .brand-dot {
    width: 64px; height: 64px; border-radius: 50%;
    background: var(--brand-blue-light);
  }
  .brand-name {
    font-weight: 700; font-size: 92px; line-height: 1;
    color: var(--ink-dark); letter-spacing: -1px;
  }
  .tagline {
    position: absolute; right: 134px; top: 262px;
    font-size: 25px; font-weight: 600; color: var(--brand-blue);
  }
  .person {
    position: absolute; left: 200px; top: 372px; width: 220px;
    text-align: right;
  }
  .person-name {
    font-size: 30px; font-weight: 700; color: var(--brand-blue);
  }
  .person-role {
    font-size: 20px; color: var(--ink-grey); margin-top: 4px;
  }
  .contact {
    position: absolute; left: 470px; top: 336px;
    font-size: 23px; line-height: 36px; color: var(--ink-grey);
  }
  .contact-label { color: var(--brand-blue); font-weight: 700; }
  .band { position: absolute; left: 0; bottom: 0; width: 1000px; height: 150px; }
</style>
</head>
<body>
  <div class="card">
    <div class="card-decor"></div>
    <div class="brand">
      <span class="brand-dot"></span>
      <span class="brand-name">wirefen.com.au</span>
    </div>
    <div class="tagline">Cloud Application Development</div>

    <div class="person">
      <div class="person-name">Liam Forbury</div>
      <div class="person-role">Technical Engineer</div>
    </div>

    <div class="contact">
      <div><span class="contact-label">Mobile:</span> 0437 125 806</div>
      <div><span class="contact-label">Email :</span> liam@wirefen.com.au</div>
      <div><span class="contact-label">Web :</span> www.wirefen.com.au</div>
    </div>

    <svg class="band" viewBox="0 0 1000 150" preserveAspectRatio="none">
      <defs>
        <linearGradient id="bandBlue" x1="0" y1="0" x2="1" y2="0">
          <stop offset="0" stop-color="var(--brand-blue)"/>
          <stop offset="0.35" stop-color="var(--brand-blue-light)"/>
          <stop offset="0.65" stop-color="var(--brand-blue)"/>
        </linearGradient>
        <clipPath id="bandShape">
          <path d="M0 120 Q500 70 1000 28 L1000 150 L0 150 Z"/>
        </clipPath>
      </defs>
      <g clip-path="url(#bandShape)">
        <rect x="0" y="0" width="1000" height="150" fill="url(#bandBlue)"/>
        <path d="M650 0 L1000 0 L1000 150 L590 150 Z" fill="var(--band-grey)"/>
      </g>
    </svg>
  </div>
</body>
</html>
```